Visitenkarte für Selbständigen
Zielgruppe
Ich bin Selbständiger Unternehmer, der sowohl Versicherungs/Finanzprodukte vertreibt, sowie Immobilien zur Kapitalanlage.
Aufgabenstellung
Ich hätte gern eine zweiseitige Karte. Vorderseite Name und meine Initialen als Logo.
Rückseite Name, Anschrift und telnr.
Berufsbezeichnung muss nicht zwingend mit auf der Karte sein.
Die Karte sollte schwarz oder weiß sein und auf der Vorderseite Name und Logo in Silber (Spiegel Folie)
Lars Hofmeier
Lindenweg 17
76829 Landau
email: info@lars-hofmeier.de
Tel 0151-38472916
Fax 06235-7281904

```html
<!DOCTYPE html>
<html lang="de">
<head>
<meta charset="utf-8">
<title>Visitenkarte Lars Hofmeier</title>
<link rel="stylesheet" href="https://fonts.googleapis.com/css2?family=Cormorant+SC:wght@500&family=Noto+Serif:wght@400&display=swap">
<style>
  :root {
    --backdrop: #6b786f;
    --card: #000000;
    --silver: #a3a3a3;
    --silver-light: #c9c9c9;
    --ink: #e6e6e6;
  }
  html, body {
    margin: 0;
    padding: 0;
    overflow: hidden;
  }
  .canvas {
    position: relative;
    width: 1017px;
    height: 1200px;
    background: var(--backdrop);
    overflow: hidden;
  }
  .card {
    position: absolute;
    top: 306px;
    width: 385px;
    height: 596px;
    background: var(--card);
    box-shadow: 8px 12px 14px rgba(0, 0, 0, 0.35);
  }
  .card--contact { left: 104px; }
  .card--brand { left: 533px; }
  .card__band {
    position: absolute;
    left: 0;
    right: 0;
    top: 394px;
    height: 19px;
    background: var(--silver);
  }
  .name {
    position: absolute;
    left: 0;
    right: 0;
    margin: 0;
    text-align: center;
    font-family: "Cormorant SC", serif;
    font-weight: 500;
    color: var(--ink);
    letter-spacing: 0.14em;
  }
  .card--contact .name--heading { top: 103px; font-size: 27px; }
  .contact {
    position: absolute;
    left: 0;
    right: 0;
    top: 166px;
    margin: 0;
    text-align: center;
    font-family: "Noto Serif", serif;
    font-style: normal;
    font-size: 16.5px;
    line-height: 26px;
    color: var(--ink);
    letter-spacing: 0.04em;
  }
  .contact__address { margin-bottom: 10px; }
  .contact p { margin: 0; }
  .wordmark {
    position: absolute;
    left: 0;
    right: 0;
    margin: 0;
    text-align: center;
    font-family: "Cormorant SC", serif;
    font-weight: 500;
    color: var(--silver);
    letter-spacing: 0.06em;
  }
  .card--contact .wordmark { top: 474px; font-size: 36px; }
  .card--brand .wordmark { top: 164px; font-size: 52px; line-height: 1.05; }
  .card--brand .name--footer { top: 465px; font-size: 26px; color: var(--silver-light); }
</style>
</head>
<body>
<main class="canvas">
  <section class="card card--contact" aria-label="Rückseite">
    <h1 class="name name--heading">Lars Hofmeier</h1>
    <address class="contact">
      <div class="contact__address">
        <p>Lindenweg 17</p>
        <p>76829 Landau</p>
      </div>
      <p>Email: info@lars-hofmeier.de</p>
      <p>Tel: 0151-38472916</p>
      <p>Fax: 06341-7281904</p>
    </address>
    <div class="card__band"></div>
    <p class="wordmark">Lars Hofmeier</p>
  </section>

  <section class="card card--brand" aria-label="Vorderseite">
    <p class="wordmark">Lars<br>Hofmeier</p>
    <div class="card__band"></div>
    <p class="name name--footer">Lars Hofmeier</p>
  </section>
</main>
</body>
</html>
```